Business software developers new website

We need to redesign our website. Our current website is http://www.plumvista.net/index.html, which is outdated and needs a new look. We moved out from web design and have concentrated more on the back end of the systems, for example, system support and security and cloud-based applications. Our major clients include both private and government sectors. We would like to see some designs that are all in one page, simple and clean. Prefer illustrator or obstructed images instead of real-life photos. Must look futuristic yet friendly. Attached the new logo for your references and good luck.

Target Market(s)

Medium to big company for their IT or data management. Either improve or upgrade their current system.

Industry/Entity Type

Business Software

Number of Pages Required

1 page

Colors

Designer to choose colors to be used in the design.

Requirements
Must have
• Simple and clean. Individual assets must be provided in the correct size and format(png or jpeg). Prefer Goggle fonts. Even though the logo color is red, grey and black, still prefer some modern colors that go well with red. When design, must consider the possibility to convert it into responsive.
Nice to have
• White background
Should not have
• real life photos, no slider

```html
<!DOCTYPE html>
<html lang="en">
<head>
<meta charset="utf-8">
<title>plumvista.net — Business Software</title>
<link href="https://fonts.googleapis.com/css2?family=Poppins:wght@600;700&family=Montserrat:wght@400;500;600;700&display=swap" rel="stylesheet">
<style>
:root{
  --red:#e52d3a;
  --black:#000;
  --ink:#1b1b1b;
  --text:#555;
  --muted:#888;
  --line:#d8d8d8;
  --soft:#f6f6f6;
  --white:#fff;
}
*{margin:0;padding:0;box-sizing:border-box}
html,body{width:1200px;height:2500px;overflow:hidden}
body{background:#fbfbfb;font-family:"Montserrat",sans-serif;color:var(--ink)}
.page{position:absolute;left:182px;top:0;width:836px;height:2500px;background:var(--white);box-shadow:0 0 8px rgba(0,0,0,.08);overflow:hidden}
.abs{position:absolute}
.eyebrow{font-size:6px;letter-spacing:2px;font-weight:600;text-transform:uppercase;color:var(--ink)}
.title{font-size:16px;font-weight:500;color:var(--ink);letter-spacing:.2px}
.body{font-size:6px;line-height:13px;color:var(--text)}
.btn{position:absolute;background:var(--red);color:var(--white);border-radius:14px;font-size:6px;font-weight:700;letter-spacing:1px;display:flex;align-items:center;justify-content:center;text-transform:uppercase}
.art{position:absolute;border-radius:6px}
.center{text-align:center;left:0;width:836px}

/* top bar */
.topbar{top:0;left:0;width:836px;height:48px;border-bottom:1px solid #e6e6e6}
.contact-mini{top:5px;font-size:5px;color:#333;display:flex;align-items:center;gap:4px}
.social{display:flex;gap:14px}
.social i{width:5px;height:5px;border-radius:50%;background:#222;display:block}
.logo{font-family:"Montserrat",sans-serif;font-weight:500;font-size:14px;color:var(--ink);display:flex;align-items:center;gap:3px}
.logo b{width:9px;height:9px;border-radius:50%;background:var(--red);display:block}
.nav{top:31px;left:470px;display:flex;gap:22px;font-size:5.5px;color:#222;letter-spacing:.3px}
.nav .active{border-bottom:1px solid #222;padding-bottom:3px}

.hero-title{top:105px;left:164px;font-family:"Poppins",sans-serif;font-weight:700;font-size:31px;line-height:47px;color:var(--black);letter-spacing:-.5px}

.feat{position:absolute;width:170px}
.feat h4{font-size:5.5px;letter-spacing:1.5px;font-weight:600;margin-left:25px}
.feat p{font-size:5.5px;line-height:13px;color:var(--text);margin-left:25px;margin-top:4px}
.feat svg{position:absolute;left:0;top:-4px}

.stats{top:942px;left:0;width:836px;height:112px;background:var(--black);color:var(--white)}
.stat{position:absolute;top:40px;text-align:center;width:130px}
.stat .num{font-family:"Poppins",sans-serif;font-weight:600;font-size:20px;display:flex;align-items:center;justify-content:center;gap:6px}
.stat .lab{font-size:5.5px;letter-spacing:1.5px;font-weight:600;margin-top:4px}

.plan{position:absolute;top:1180px;width:160px;height:207px;background:var(--black);color:var(--white);text-align:center}
.plan.pro{background:var(--red)}
.plan .name{font-size:6px;letter-spacing:2px;margin-top:25px}
.plan .desc{font-size:6px;margin-top:8px}
.plan hr{border:0;border-top:1px solid rgba(255,255,255,.7);width:100px;margin:10px auto 0}
.plan .price{font-family:"Poppins",sans-serif;font-weight:600;font-size:26px;margin-top:6px}
.plan .price sup{font-size:10px}
.plan .per{font-size:5.5px;letter-spacing:1px}
.plan .feat-t{font-size:5.5px;line-height:13px;margin-top:8px}
.plan .cta{width:84px;height:22px;border:1px solid var(--white);border-radius:12px;margin:12px auto 0;font-size:5.5px;letter-spacing:1.5px;display:flex;align-items:center;justify-content:center}

.testi{top:1423px;left:0;width:836px;height:247px;background:var(--soft)}
.blog{top:1670px;left:0;width:836px;height:351px;background:var(--black);color:var(--white)}
.post{position:absolute;top:159px;width:160px;height:156px;background:linear-gradient(135deg,#b9b2a9,#6f6a64)}
.post .tag{position:absolute;top:19px;left:19px;background:var(--black);color:var(--white);font-size:5.5px;letter-spacing:.5px;padding:3px 7px;border-radius:8px}
.post .cap{position:absolute;left:8px;right:8px;bottom:12px;background:rgba(255,255,255,.85);color:var(--ink);padding:6px 12px}
.post .meta{font-size:4.5px;color:#555}
.post .head{font-size:7px;font-weight:700;line-height:13px;letter-spacing:.2px}

.field{position:absolute;left:126px;width:274px;border-bottom:1px solid #999;font-size:6px;color:#333;padding-bottom:4px}

.foot-h{font-size:5.5px;letter-spacing:2px;font-weight:600}
.foot-l{font-size:5px;color:#555;line-height:17px}
.foot-row{display:flex;align-items:center;gap:10px}
.foot-row i{width:6px;height:6px;background:#333;border-radius:50%;display:block}
</style>
</head>
<body>
<div class="page">

  <!-- top bar -->
  <header class="abs topbar">
    <div class="abs contact-mini" style="left:163px">
      <svg width="6" height="6" viewBox="0 0 10 10"><path d="M2 1l2 2-1 1.5c.8 1.5 1.8 2.5 3.3 3.3L7.8 6.8l2 2-1.3 1.2C4.5 9.7.3 5.5 0 1.5z" fill="#222"/></svg>+61 7 5550 0142</div>
    <div class="abs contact-mini" style="left:234px">
      <svg width="7" height="5" viewBox="0 0 12 8"><rect width="12" height="8" fill="#222"/><path d="M0 0l6 4 6-4" stroke="#fff" fill="none"/></svg>info@plumvista.net</div>
    <div class="abs contact-mini" style="left:316px">
      <svg width="5" height="7" viewBox="0 0 8 11"><path d="M4 0a4 4 0 0 1 4 4c0 3-4 7-4 7S0 7 0 4a4 4 0 0 1 4-4z" fill="#222"/><circle cx="4" cy="4" r="1.5" fill="#fff"/></svg>48, orchard lane, avondale</div>
    <div class="abs social" style="left:612px;top:7px"><i></i><i></i><i></i><i></i></div>
    <div class="abs logo" style="left:163px;top:27px">plum<b></b>vista.net</div>
    <nav class="abs nav">
      <span class="active">HOME</span><span>ABOUT</span><span>SERVICES</span><span>BLOG</span><span>CONTACTS</span>
    </nav>
  </header>

  <!-- hero -->
  <h1 class="abs hero-title">Create stories for the<br>digital corporate</h1>
  <div class="btn" style="left:164px;top:231px;width:106px;height:25px">More about us</div>
  <div class="art" role="img" aria-label="Isometric illustration of a team building a mobile app on a large phone" style="left:478px;top:68px;width:300px;height:282px;background:radial-gradient(circle at 55% 45%,#dfe6f7 0%,#eef2f8 55%,#fff 75%)"></div>

  <!-- about -->
  <div class="art" role="img" aria-label="Illustration of a desk with a lamp, laptop and plant" style="left:115px;top:393px;width:272px;height:165px;background:radial-gradient(circle at 50% 50%,#eef1f5 0%,#fff 70%)"></div>
  <div class="abs eyebrow" style="left:455px;top:370px">About us</div>
  <h2 class="abs title" style="left:455px;top:383px;letter-spacing:1px">Who We Are</h2>
  <div class="abs" style="left:455px;top:410px;width:95px;height:2px;background:var(--black)"></div>
  <p class="abs body" style="left:455px;top:427px;width:205px">We have provided web design, graphic design and application development solutions for a wide variety of industries. We are known for the quality of our work, affordable rates and our individual approach to each customer. Our company offers a wide variety of professional web solution and all this at very competitive prices!</p>
  <div class="btn" style="left:455px;top:526px;width:88px;height:25px">Read more</div>

  <!-- features -->
  <div class="abs eyebrow" style="left:164px;top:688px">Our features</div>
  <h2 class="abs title" style="left:164px;top:700px">Why Businesses Choose Us</h2>
  <div class="abs" style="left:164px;top:720px;width:210px;height:1px;background:var(--black)"></div>
  <p class="abs body" style="left:164px;top:746px;width:290px">If you are looking for a trusted and experienced partner to help you with decision-making in your business, Plumvista is the right place for you!</p>

  <div class="feat" style="left:164px;top:794px">
    <svg width="18" height="20" viewBox="0 0 18 20"><circle cx="9" cy="8" r="6" fill="none" stroke="#222"/><rect x="6" y="14" width="6" height="4" fill="none" stroke="#222"/></svg>
    <h4>INNOVATIVE SOLUTIONS</h4><p>We stand for fresh view on business and implement novelties with pleasure.</p></div>
  <div class="feat" style="left:338px;top:794px">
    <svg width="18" height="20" viewBox="0 0 18 20"><circle cx="9" cy="9" r="6" fill="none" stroke="#222"/><circle cx="9" cy="9" r="2" fill="#222"/></svg>
    <h4>QUALITY RESOURCING</h4><p>We strive to use modern technologies and the latest resources in our work.</p></div>
  <div class="feat" style="left:164px;top:850px">
    <svg width="20" height="20" viewBox="0 0 20 20"><circle cx="10" cy="10" r="8" fill="none" stroke="#222"/><circle cx="10" cy="10" r="4" fill="none" stroke="#222"/><path d="M10 10l8-8" stroke="#222"/></svg>
    <h4>EXPERIENCED CONSULTANTS</h4><p>Every team member has over five years of experience in business.</p></div>
  <div class="feat" style="left:338px;top:850px">
    <svg width="20" height="20" viewBox="0 0 20 20"><circle cx="10" cy="5" r="3" fill="none" stroke="#222"/><path d="M3 18c0-5 3-8 7-8s7 3 7 8z" fill="none" stroke="#222"/></svg>
    <h4>SOLUTION DEFINING</h4><p>When you don't see the right decision, we are here to show you ones.</p></div>

  <div class="art" role="img" aria-label="Illustration of a laptop with a cloud, chat bubbles and a globe" style="left:488px;top:698px;width:291px;height:180px;background:radial-gradient(circle at 50% 50%,#d6e6ea 0%,#eef4f6 50%,#fff 75%)"></div>

  <!-- stats -->
  <section class="abs stats">
    <div class="stat" style="left:163px">
      <div class="num"><svg width="18" height="18" viewBox="0 0 18 18"><path d="M3 17V8l6-5 6 5v9z" fill="none" stroke="#fff"/></svg>2007</div>
      <div class="lab">COMPANY ESTABLISHED</div></div>
    <div class="stat" style="left:293px">
      <div class="num"><svg width="18" height="16" viewBox="0 0 18 16"><rect x="1" y="1" width="16" height="11" fill="none" stroke="#fff"/><path d="M6 15h6" stroke="#fff"/></svg>547</div>
      <div class="lab">SUCCESS PROJECTS</div></div>
    <div class="stat" style="left:423px">
      <div class="num"><svg width="18" height="16" viewBox="0 0 18 16"><path d="M1 10l5-5 4 3 7-7" fill="none" stroke="#fff"/></svg>45+</div>
      <div class="lab">BUSINESS PARTNERS</div></div>
    <div class="stat" style="left:555px">
      <div class="num"><svg width="20" height="16" viewBox="0 0 20 16"><circle cx="6" cy="5" r="3" fill="none" stroke="#fff"/><circle cx="14" cy="5" r="3" fill="none" stroke="#fff"/><path d="M1 15c0-4 2-6 5-6s5 2 5 6M9 15c0-4 2-6 5-6s5 2 5 6" fill="none" stroke="#fff"/></svg>1500</div>
      <div class="lab">HAPPY CLIENTS</div></div>
  </section>

  <!-- pricing -->
  <div class="abs eyebrow center" style="top:1089px">Thing are good enough</div>
  <h2 class="abs title center" style="top:1100px">Find the Perfect Plan for Your Business</h2>
  <p class="abs body" style="top:1131px;left:275px;width:286px;text-align:center">If you are looking for a trusted and experienced partner to help you with decision-making in your business, Plumvista is the right place for you!</p>

  <div class="plan" style="left:164px">
    <div class="name">STARTER</div><div class="desc">Here goes some description</div><hr>
    <div class="price"><sup>$</sup>39</div><div class="per">MONTHLY</div>
    <div class="feat-t">Create excepteur sint occaecat<br>cupidatat non proident</div>
    <div class="cta">GET STARTED</div></div>
  <div class="plan pro" style="left:338px">
    <div class="name">PRO PLAN</div><div class="desc">Here goes some description</div><hr>
    <div class="price"><sup>$</sup>69</div><div class="per">MONTHLY</div>
    <div class="feat-t">Create excepteur sint occaecat<br>cupidatat non proident</div>
    <div class="cta">GET STARTED</div></div>
  <div class="plan" style="left:512px">
    <div class="name">ENTERPRISE PLAN</div><div class="desc">Here goes some description</div><hr>
    <div class="price"><sup>$</sup>89</div><div class="per">MONTHLY</div>
    <div class="feat-t">Create excepteur sint occaecat<br>cupidatat non proident</div>
    <div class="cta">GET STARTED</div></div>

  <!-- testimonials -->
  <section class="abs testi">
    <div class="abs eyebrow center" style="top:37px">Testimonials</div>
    <h2 class="abs title center" style="top:49px">What People Say About Us</h2>
    <p class="abs body" style="top:82px;left:250px;width:336px;text-align:center">Donec vitae sapien ut libero venenatis faucibus. Nullam quis ante. Etiam sit amet orci eget eros faucibus tincidunt. Duis leo. Sed fringilla mauris sit amet nibh. Donec sodales sagittis magna. Sed consequat, leo eget bibendum sodales, augue velit cursus nunc,</p>
    <div class="abs" role="img" aria-label="Client portrait" style="left:396px;top:131px;width:44px;height:44px;border-radius:50%;border:2px solid #333;background:linear-gradient(#c9c4be,#8e8781)"></div>
    <div class="abs center" style="top:182px;font-size:7px;font-weight:700">Marcus Hollin</div>
    <div class="abs center" style="top:194px;font-size:6px;color:#555">Product Manager</div>
    <div class="abs" style="left:407px;top:212px;display:flex;gap:5px">
      <i style="width:3px;height:3px;border-radius:50%;background:#222;display:block"></i>
      <i style="width:3px;height:3px;border-radius:50%;border:1px solid #222;display:block"></i>
      <i style="width:3px;height:3px;border-radius:50%;border:1px solid #222;display:block"></i>
    </div>
  </section>

  <!-- blog -->
  <section class="abs blog">
    <div class="abs eyebrow center" style="top:38px;color:#fff">Our blog</div>
    <h2 class="abs title center" style="top:55px;color:#fff">Recent News</h2>
    <p class="abs center" style="top:95px;font-size:6px;line-height:13px;font-weight:600;letter-spacing:-.2px">We want to share with you the latest news in world financial and business spheres, so you could be<br>always ready for economical changes!</p>
    <div class="post" role="img" aria-label="Photo area: team meeting in an office" style="left:164px">
      <span class="tag">BUSINESS</span>
      <div class="cap"><div class="meta">ADMIN MAY 20, 2019</div><div class="head">Software Defined Networking<br>in Business Security</div></div></div>
    <div class="post" role="img" aria-label="Photo area: handshake over a laptop" style="left:338px;background:linear-gradient(135deg,#7a746d,#3d3a37)">
      <span class="tag">BUSINESS</span>
      <div class="cap"><div class="meta">ADMIN MAY 20, 2019</div><div class="head">Software Defined Networking<br>in Business Security</div></div></div>
    <div class="post" role="img" aria-label="Photo area: hands reviewing documents beside a laptop" style="left:512px;background:linear-gradient(135deg,#b8c2c8,#6d7a82)">
      <span class="tag">BUSINESS</span>
      <div class="cap"><div class="meta">ADMIN MAY 20, 2019</div><div class="head">Software Defined Networking<br>in Business Security</div></div></div>
  </section>

  <!-- contact -->
  <div class="abs eyebrow" style="left:126px;top:2071px">Contact us</div>
  <h2 class="abs title" style="left:126px;top:2083px">Let's Work Together</h2>
  <p class="abs body" style="left:126px;top:2111px;width:240px">Now we are a leading company in business consulting and provide a great bulk of services and packages to our clients.</p>
  <div class="field" style="top:2152px">Name</div>
  <div class="field" style="top:2183px">E-mail</div>
  <div class="field" style="top:2214px;height:45px">Message</div>
  <div class="btn" style="left:126px;top:2280px;width:88px;height:24px">Send message</div>
  <div class="art" role="img" aria-label="Embedded road map of the office area" style="left:425px;top:2021px;width:411px;height:311px;border-radius:0;background:linear-gradient(160deg,#eceae4,#e4e6df)"></div>

  <!-- footer -->
  <footer>
    <div class="abs logo" style="left:164px;top:2352px">plum<b></b>vista.net</div>
    <p class="abs foot-l" style="left:164px;top:2370px;width:118px;line-height:9.5px;font-size:5.5px">As web developers, we understand that a powerful and functional web site is a vital component of modern day marketing for companies of today. This is why our web site development team work with all of our clients to ensure their web site design will deliver to their target market.</p>

    <div class="abs foot-h" style="left:294px;top:2357px">CONTACT INFO</div>
    <div class="abs foot-l" style="left:294px;top:2370px">
      <div class="foot-row"><i></i>+61 7 5550 0142</div>
      <div class="foot-row"><i></i>email@plumvista.net</div>
      <div class="foot-row"><i></i>www.plumvista.net/contact.html</div>
      <div class="foot-row"><i></i>4780 Ridge Road</div>
    </div>

    <div class="abs foot-h" style="left:425px;top:2357px">QUICK LINKS</div>
    <div class="abs foot-l" style="left:425px;top:2370px">Home<br>About<br>Services<br>Blog<br>Contacts</div>

    <div class="abs foot-h" style="left:512px;top:2357px">NEWSLETTER</div>
    <div class="abs" style="left:512px;top:2376px;width:160px;height:20px;border-radius:10px;background:#555;color:#fff;font-size:5.5px;display:flex;align-items:center;padding-left:14px">Your Email Address</div>
    <div class="btn" style="left:622px;top:2376px;width:50px;height:20px;font-size:5.5px">Sign up</div>
    <p class="abs foot-l" style="left:512px;top:2404px;width:160px;line-height:13px">Be the first to find out about exclusive deals, the latest Lookbooks, and top trends.</p>

    <div class="abs" style="left:164px;top:2484px;font-size:5.5px;color:#222">© 2019 Plumvista.net. All rights reserved. Terms and Conditions</div>
    <div class="abs social" style="left:612px;top:2486px"><i></i><i></i><i></i><i></i></div>
  </footer>

</div>
</body>
</html>
```